Dornel Letterhead

Hi I really like the attached pictures for our business cards could you please look at designing something similar for our letterheads and stationary.

The details on our letterhead will be

Dornel Pty Ltd
ABN 847 216 350
PO Box 7184
Marlow Vale NSW 2163
0468 137 926
office"dornel.com.au

```html
<!DOCTYPE html>
<html lang="en">
<head>
<meta charset="utf-8">
<title>Dornel Letterhead</title>
<link href="https://fonts.googleapis.com/css2?family=Tinos:wght@400&family=Roboto:wght@400;500;700&display=swap" rel="stylesheet">
<style>
  :root {
    --paper: #f1f1f3;
    --ink: #2d2d2d;
    --body-ink: #3a3a3a;
    --muted: #555555;
    --brand-blue: #3d7cc9;
    --band-black: #050505;
    --rule: #b9b9bd;
    --signature-tone: #dcdce2;
  }
  html, body {
    margin: 0;
    padding: 0;
    width: 879px;
    height: 1200px;
    overflow: hidden;
    background: var(--paper);
  }
  .letterhead {
    position: relative;
    width: 879px;
    height: 1200px;
    background: var(--paper);
    overflow: hidden;
    font-family: "Tinos", "Times New Roman", serif;
    color: var(--ink);
  }
  .band {
    position: absolute;
    left: 0;
    width: 879px;
  }
  .band--top { top: 0; height: 34px; }
  .band--bottom { bottom: 0; height: 50px; }

  .brand {
    position: absolute;
    left: 110px;
    top: 136px;
    display: flex;
    align-items: center;
    gap: 12px;
  }
  .brand__mark {
    width: 24px;
    height: 24px;
    background: var(--brand-blue);
  }
  .brand__name {
    font-family: "Roboto", Arial, sans-serif;
    font-weight: 700;
    font-size: 50px;
    line-height: 1;
    color: var(--ink);
  }

  .contact {
    position: absolute;
    left: 637px;
    top: 84px;
    padding-left: 14px;
    border-left: 1px solid var(--rule);
    font-family: "Roboto", Arial, sans-serif;
    font-style: normal;
    font-size: 12.5px;
    line-height: 14.8px;
    color: var(--muted);
  }
  .contact__company,
  .contact__web { color: var(--brand-blue); font-weight: 500; }

  .letter {
    position: absolute;
    left: 100px;
    width: 682px;
    color: var(--body-ink);
  }
  .letter__date { top: 300px; font-size: 15px; line-height: 20px; }
  .letter__recipient { top: 404px; font-size: 15px; line-height: 20px; }
  .letter__recipient { top: 362px; }
  .letter__body { top: 468px; font-size: 13.4px; line-height: 20px; }
  .letter__body p { margin: 0 0 20px; text-align: justify; }

  .signature {
    position: absolute;
    left: 108px;
    top: 830px;
    width: 165px;
    height: 66px;
    border-radius: 33px;
    background: radial-gradient(ellipse at center, var(--signature-tone), rgba(241,241,243,0) 70%);
  }
</style>
</head>
<body>
<main class="letterhead">
  <svg class="band band--top" viewBox="0 0 879 34" preserveAspectRatio="none" aria-hidden="true">
    <polygon points="0,0 879,0 879,34 0,2" fill="var(--brand-blue)"/>
  </svg>

  <div class="brand">
    <span class="brand__mark"></span>
    <span class="brand__name">Dornel</span>
  </div>

  <address class="contact">
    <div class="contact__company">Dornel Pty Ltd</div>
    <div>PO Box 7184</div>
    <div>Marlow Vale NSW 2163</div>
    <div>P : 0468 137 926</div>
    <div>E : office@dornel.com.au</div>
    <div>ABN : 847 216 350</div>
    <div class="contact__web">www.dornel.com.au</div>
  </address>

  <div class="letter letter__date">Cartagena de Indias, Ocober 12,2015</div>

  <div class="letter letter__recipient">
    Sr.<br>TOMAS AREVALO<br>Web Master<br>City
  </div>

  <div class="letter letter__body">
    <p>Contrary to popular belief, Lorem Ipsum is not simply random text. It has roots in a piece of classical Latin literature from 45 BC, making it over 2000 years old. Edwin Harlow, a Latin professor at Westbridge College in Virginia, looked up one of the more obscure Latin words, consectetur, from a Lorem Ipsum passage, and going through the cites of the word in classical literature,</p>
    <p>discovered the undoubtable source. Lorem Ipsum comes from sections 1.10.32 and 1.10.33 of "de Finibus Bonorum et Malorum" (The Extremes of Good and Evil) by Cicero, written in 45 BC. This book is a treatise on the theory of ethics, very popular during the Renaissance. The first line of Lorem Ipsum, "Lorem ipsum dolor sit amet..", comes from a line in section 1.10.32.</p>
    <p>The standard chunk of Lorem Ipsum used since the 1500s is reproduced below for those interested. Sections 1.10.32 and 1.10.33 from "de Finibus Bonorum et Malorum" by Cicero are also reproduced in their exact original form, accompanied by English versions from the 1914 translation by H. Linwood.</p>
    <p>There are many variations of passages of Lorem Ipsum available, but the majority have suffered alteration in some form, by injected humour, or randomised words which don't look even slightly believable. If you are going to use a passage of Lorem Ipsum, you need to be sure there isn't anything embarrassing hidden in the middle of text.</p>
  </div>

  <div class="signature" role="img" aria-label="Handwritten signature of Martin Kell"></div>

  <svg class="band band--bottom" viewBox="0 0 879 50" preserveAspectRatio="none" aria-hidden="true">
    <polygon points="0,0 879,12 879,50 0,50" fill="var(--band-black)"/>
  </svg>
</main>
</body>
</html>
```